Need DL Flyer for Real Estate Drops

We need a real estate flyer ,double sided. With content on 1 side like: Want to know what's your house is worth " contact us today and on other side agent details. We are looking for an ongoing partnership with designer so this assignment will be ongoing

```html
<!DOCTYPE html>
<html lang="en">
<head>
<meta charset="utf-8">
<title>Mirada Realty – DL Flyer</title>
<link href="https://fonts.googleapis.com/css2?family=Poppins:wght@400;500;600;700;800&display=swap" rel="stylesheet">
<style>
  :root{
    --red:#c81e27;
    --navy:#131b36;
    --white:#ffffff;
    --page:#e9e9e9;
    --text-dark:#1b1d2a;
    --room-light:#d9d2c8;
    --room-mid:#a69d94;
    --room-dark:#4a4750;
    --home-sky:#b9d0e8;
    --home-wall:#b7a48e;
    --home-lawn:#7f9a5e;
  }
  *{box-sizing:border-box;margin:0;padding:0}
  html,body{width:685px;height:1200px;overflow:hidden}
  body{background:var(--page);font-family:'Poppins',sans-serif;position:relative}
  .flyer{position:absolute;top:274px;width:310px;height:651px;overflow:hidden;box-shadow:0 6px 16px rgba(0,0,0,.25)}
  .flyer--front{left:20px}
  .flyer--back{left:355px;background:var(--white)}
  .flyer__art{position:absolute;inset:0;width:310px;height:651px}
  .txt{position:absolute;line-height:1.15}

  /* front */
  .brand{position:absolute;top:26px;left:0;width:310px;display:flex;justify-content:center;align-items:center;gap:10px;z-index:2}
  .brand__mark{width:34px;height:34px;background:var(--navy)}
  .brand__name{font-size:29px;font-weight:600;color:var(--white);letter-spacing:-.5px;line-height:1}
  .headline-kicker{top:303px;left:30px;font-size:15px;font-weight:700;color:var(--white)}
  .headline{top:338px;left:28px;font-size:37px;font-weight:800;line-height:.98;letter-spacing:-.5px}
  .headline__red{color:var(--red);display:block}
  .headline__navy{color:var(--navy);display:block}
  .dots{display:flex;gap:3px}
  .dots i{width:6px;height:6px;border-radius:50%;background:var(--navy)}
  .dots i:nth-child(3){background:#7a8196}
  .dots i:nth-child(4){background:#c3c7d1}
  .front-dots{top:418px;left:31px}
  .pitch-title{top:430px;left:30px;font-size:11.5px;font-weight:600;color:var(--navy)}
  .pitch-title span{color:var(--red)}
  .pitch-body{top:448px;left:30px;width:192px;font-size:8.6px;line-height:1.28;color:var(--text-dark)}
  .contact-bar{position:absolute;top:547px;left:32px;width:2px;height:34px;background:#4b78c8}
  .contact-kicker{top:546px;left:40px;font-size:8.5px;font-weight:600;color:var(--red)}
  .contact-today{top:556px;left:40px;font-size:22px;font-weight:700;color:var(--white)}
  .contact-phone{top:588px;left:30px;font-size:17px;font-weight:600;color:var(--white);display:flex;align-items:center;gap:3px}
  .contact-line{left:30px;font-size:8.2px;color:var(--white);display:flex;align-items:center;gap:5px}
  .contact-line--mail{top:614px}
  .contact-line--pin{top:627px}
  .icon{flex:none}

  /* back */
  .back-kicker{top:318px;left:32px;font-size:12px;font-weight:700;color:var(--navy)}
  .back-today{top:328px;left:30px;font-size:29px;font-weight:800;color:var(--red)}
  .quote{font-size:26px;font-weight:700;color:var(--red);line-height:1}
  .quote--open{top:368px;left:29px}
  .quote--close{top:432px;left:116px}
  .motto{top:384px;left:30px;width:112px;font-size:10.8px;font-weight:500;color:var(--navy);line-height:1.2}
  .agent-name{top:486px;left:29px;font-size:22px;font-weight:800;color:var(--white);letter-spacing:-.3px}
  .agent-name span{color:var(--navy)}
  .agent-role{top:513px;left:29px;font-size:11px;color:var(--white);line-height:1.2}
  .back-dots{top:547px;left:30px}
  .back-dots i{background:var(--navy)}
  .back-dots i:nth-child(3),.back-dots i:nth-child(4){background:#7c1218}
  .agent-line{left:29px;font-size:11.5px;font-weight:500;color:var(--white);display:flex;align-items:center;gap:5px}
  .agent-line--phone{top:559px}
  .agent-line--web{top:576px}
  .agent-line--mail{top:591px}
  .agent-line--pin{top:607px}
  .sep{display:inline-block;width:1px;height:12px;background:var(--white);margin:0 4px}
</style>
</head>
<body>

<section class="flyer flyer--front">
  <svg class="flyer__art" viewBox="0 0 310 651">
    <defs>
      <linearGradient id="sky" x1="0" y1="0" x2="0" y2="1">
        <stop offset="0" stop-color="#b7cfe8"/>
        <stop offset="1" stop-color="#f5f8fc"/>
      </linearGradient>
      <linearGradient id="interior" x1="0" y1="0" x2="0" y2="1">
        <stop offset="0" stop-color="var(--room-light)"/>
        <stop offset=".55" stop-color="var(--room-mid)"/>
        <stop offset="1" stop-color="var(--room-dark)"/>
      </linearGradient>
      <linearGradient id="house" x1="0" y1="0" x2="0" y2="1">
        <stop offset="0" stop-color="#8e939c"/>
        <stop offset=".4" stop-color="#eceae6"/>
        <stop offset="1" stop-color="#c9a57e"/>
      </linearGradient>
    </defs>
    <rect width="310" height="651" fill="url(#sky)"/>
    <rect y="330" width="310" height="140" fill="#ffffff" opacity=".55"/>
    <rect class="red-top" width="310" height="172" fill="var(--red)"/>
    <rect y="120" width="110" height="52" fill="#b51a22"/>
    <path role="img" aria-label="Photo of a smiling agent pointing down in a bright living room with a sofa"
      d="M0 172 H70 C96 172 106 158 112 132 C118 106 132 92 162 92 H310 V205 C300 250 270 278 215 280 H0 Z" fill="url(#interior)"/>
    <path class="wave-band" d="M0 280 H215 C268 278 302 245 310 200 V235 C300 300 258 335 200 335 H0 Z" fill="var(--navy)"/>
    <path role="img" aria-label="Photo of a modern two-storey house with a pitched roof and balcony"
      d="M230 420 C260 412 290 408 310 412 V651 H232 C228 600 222 560 218 520 C214 470 214 430 230 420 Z" fill="url(#house)"/>
    <path class="contact-panel" d="M0 528 H165 C215 528 245 565 262 651 H0 Z" fill="var(--navy)"/>
  </svg>

  <div class="brand"><span class="brand__mark"></span><span class="brand__name">Mirada Realty</span></div>
  <p class="txt headline-kicker">WHAT IS YOUR</p>
  <h1 class="txt headline"><span class="headline__red">HOUSE</span><span class="headline__navy">WORTH</span></h1>
  <div class="txt dots front-dots"><i></i><i></i><i></i><i></i></div>
  <p class="txt pitch-title">Thinking of <span>selling a property?</span></p>
  <p class="txt pitch-body">In case you're planning to sell a property, contact us and we make sure to get the best possible conditions for you. Setting up the exposé and professional real estate photography are free of charge.</p>

  <span class="contact-bar"></span>
  <p class="txt contact-kicker">CONTACT US</p>
  <p class="txt contact-today">TODAY!</p>
  <p class="txt contact-phone">
    <svg class="icon" width="11" height="11" viewBox="0 0 24 24"><path d="M6.6 10.8a15.1 15.1 0 0 0 6.6 6.6l2.2-2.2a1 1 0 0 1 1-.25 11.4 11.4 0 0 0 3.6.57 1 1 0 0 1 1 1V20a1 1 0 0 1-1 1A17 17 0 0 1 3 4a1 1 0 0 1 1-1h3.5a1 1 0 0 1 1 1c0 1.25.2 2.45.57 3.57a1 1 0 0 1-.25 1z" fill="var(--red)"/></svg>
    03 9100 2200
  </p>
  <p class="txt contact-line contact-line--mail">
    <svg class="icon" width="8" height="6" viewBox="0 0 16 12"><rect width="16" height="12" fill="var(--red)"/><path d="M0 0 L8 7 L16 0" stroke="var(--navy)" fill="none" stroke-width="1.5"/></svg>
    info@miradarealty.com.au
  </p>
  <p class="txt contact-line contact-line--pin">
    <svg class="icon" width="7" height="9" viewBox="0 0 12 16"><path d="M6 0a6 6 0 0 1 6 6c0 4.5-6 10-6 10S0 10.5 0 6a6 6 0 0 1 6-6z" fill="var(--red)"/><circle cx="6" cy="6" r="2.2" fill="var(--navy)"/></svg>
    14/8 Harbour Ln, Westfield, VIC 3000
  </p>
</section>

<section class="flyer flyer--back">
  <svg class="flyer__art" viewBox="0 0 310 651">
    <defs>
      <linearGradient id="skyBack" x1="0" y1="0" x2="0" y2="1">
        <stop offset="0" stop-color="#ffffff"/>
        <stop offset=".3" stop-color="#ffffff"/>
        <stop offset=".5" stop-color="#cfdff0"/>
        <stop offset=".75" stop-color="#e9f1f9"/>
        <stop offset="1" stop-color="#dbe7f3"/>
      </linearGradient>
      <linearGradient id="home" x1="0" y1="0" x2="0" y2="1">
        <stop offset="0" stop-color="var(--home-sky)"/>
        <stop offset=".35" stop-color="#d6dde6"/>
        <stop offset=".7" stop-color="var(--home-wall)"/>
        <stop offset="1" stop-color="var(--home-lawn)"/>
      </linearGradient>
      <linearGradient id="agent" x1="0" y1="0" x2="0" y2="1">
        <stop offset="0" stop-color="#d5e2ef"/>
        <stop offset=".45" stop-color="#8b9abb"/>
        <stop offset="1" stop-color="#1d2a58"/>
      </linearGradient>
    </defs>
    <rect width="310" height="651" fill="url(#skyBack)"/>
    <path class="corner-band" d="M0 0 H310 V9 H75 C35 9 22 35 22 65 V88 H0 Z" fill="var(--navy)"/>

    <path role="img" aria-label="Photo of a sold contemporary timber and glass house" d="M67 45 H146 V124 Q146 159 111 159 H32 V80 Q32 45 67 45 Z" fill="url(#home)"/>
    <path role="img" aria-label="Photo of a sold two-storey family home with a lawn" d="M198 45 H277 V124 Q277 159 242 159 H163 V80 Q163 45 198 45 Z" fill="url(#home)"/>
    <path role="img" aria-label="Photo of a sold contemporary timber and glass house" d="M67 177 H146 V256 Q146 291 111 291 H32 V212 Q32 177 67 177 Z" fill="url(#home)"/>

    <g class="sold-ribbon">
      <polygon points="92,40 116,40 152,76 152,100" fill="var(--red)"/>
      <text x="128" y="73" transform="rotate(45 128 73)" font-family="Poppins, sans-serif" font-weight="700" font-size="12" fill="#fff" text-anchor="middle">SOLD</text>
      <polygon points="223,40 247,40 283,76 283,100" fill="var(--red)"/>
      <text x="259" y="73" transform="rotate(45 259 73)" font-family="Poppins, sans-serif" font-weight="700" font-size="12" fill="#fff" text-anchor="middle">SOLD</text>
      <polygon points="92,172 116,172 152,208 152,232" fill="var(--red)"/>
      <text x="128" y="205" transform="rotate(45 128 205)" font-family="Poppins, sans-serif" font-weight="700" font-size="12" fill="#fff" text-anchor="middle">SOLD</text>
    </g>

    <path role="img" aria-label="Portrait of the agent in a navy suit and striped tie"
      d="M200 180 H310 V560 H145 C150 470 160 400 185 340 C190 320 192 300 192 280 V190 Q192 180 200 180 Z" fill="url(#agent)" opacity=".9"/>

    <path class="contact-panel" d="M0 468 H215 C262 468 298 515 310 585 V651 H0 Z" fill="var(--red)"/>
  </svg>

  <p class="txt back-kicker">CONTACT US</p>
  <p class="txt back-today">TODAY!</p>
  <p class="txt quote quote--open">“</p>
  <p class="txt motto">Real Estate is not just about selling and leasing, it's about relationships</p>
  <p class="txt quote quote--close">”</p>

  <h2 class="txt agent-name">DANIEL <span>ROWE</span></h2>
  <p class="txt agent-role">Managing Director/LEA, Mirada<br>Realty</p>
  <div class="txt dots back-dots"><i></i><i></i><i></i><i></i></div>
  <p class="txt agent-line agent-line--phone">
    <svg class="icon" width="10" height="10" viewBox="0 0 24 24"><path d="M6.6 10.8a15.1 15.1 0 0 0 6.6 6.6l2.2-2.2a1 1 0 0 1 1-.25 11.4 11.4 0 0 0 3.6.57 1 1 0 0 1 1 1V20a1 1 0 0 1-1 1A17 17 0 0 1 3 4a1 1 0 0 1 1-1h3.5a1 1 0 0 1 1 1c0 1.25.2 2.45.57 3.57a1 1 0 0 1-.25 1z" fill="var(--navy)"/></svg>
    03 9100 2200<span class="sep"></span>
    <svg class="icon" width="7" height="10" viewBox="0 0 10 16"><rect x="1" y="0" width="8" height="16" rx="1.5" fill="var(--navy)"/><rect x="2.5" y="2" width="5" height="10" fill="var(--red)"/></svg>
    0400 123 456
  </p>
  <p class="txt agent-line agent-line--web">
    <svg class="icon" width="10" height="10" viewBox="0 0 16 16"><circle cx="8" cy="8" r="7" fill="none" stroke="var(--navy)" stroke-width="1.6"/><path d="M1 8 H15 M8 1 C4 5 4 11 8 15 M8 1 C12 5 12 11 8 15" fill="none" stroke="var(--navy)" stroke-width="1.2"/></svg>
    www.miradarealty.com.au
  </p>
  <p class="txt agent-line agent-line--mail">
    <svg class="icon" width="10" height="8" viewBox="0 0 16 12"><rect width="16" height="12" fill="var(--navy)"/><path d="M0 0 L8 7 L16 0" stroke="var(--red)" fill="none" stroke-width="1.5"/></svg>
    daniel@miradarealty.com.au
  </p>
  <p class="txt agent-line agent-line--pin">
    <svg class="icon" width="9" height="11" viewBox="0 0 12 16"><path d="M6 0a6 6 0 0 1 6 6c0 4.5-6 10-6 10S0 10.5 0 6a6 6 0 0 1 6-6z" fill="var(--navy)"/><circle cx="6" cy="6" r="2.2" fill="var(--red)"/></svg>
    14/8 Harbour Ln, Westfield, VIC 3000
  </p>
</section>

</body>
</html>
```